Hemp company needs website/online store

We are a startup hemp company and we need an online storefront designed. We are very open do design, but will include our logo to help. We make 100% hemp derived products like edibles, concentrates, vapes and THCA flower. Everything is grown locally, and all products are extracted and made in house.

Requirements
Nice to have
• I would like to highlight that we have Cannabis products that are hemp derived and 100% legal across the US. Also that all cannabis is locally grown and products are extracted and made in house and sent out for third party lab testing.

```html
<!DOCTYPE html>
<html lang="en">
<head>
<meta charset="utf-8">
<title>Meadowbright Hemp</title>
<link rel="stylesheet" href="https://fonts.googleapis.com/css2?family=Poppins:wght@400;500;600;700&family=Playfair+Display:ital,wght@1,500&display=swap">
<style>
:root{
  --orange:#f7a21b;
  --green:#3f7137;
  --leaf:#6aa32f;
  --dark:#0d0e0c;
  --footer:#181a15;
  --card:#eef0e8;
  --paper:#f4f4f2;
  --ink:#1e1e1e;
  --muted:#7a7a7a;
  --white:#ffffff;
}
*{box-sizing:border-box;margin:0;padding:0}
html,body{width:1200px;height:3296px;overflow:hidden}
body{position:relative;font-family:"Poppins",sans-serif;color:var(--ink);background:var(--white)}
.abs{position:absolute}

/* Header + hero */
.hero{position:absolute;left:0;top:0;width:1200px;height:598px;background:var(--dark)}
.hero-photo{position:absolute;right:0;top:0;width:620px;height:598px;
  background:radial-gradient(ellipse at 70% 40%,#3f7a2a 0%,#1f4a18 35%,#0d1a0b 70%,rgba(13,14,12,0) 100%)}
.topbar{position:absolute;left:0;top:0;width:1200px;height:108px;background:rgba(20,20,18,.85)}
.brand{position:absolute;display:flex;align-items:center;gap:10px;font-weight:600;color:var(--leaf)}
.brand .mark{width:22px;height:22px;background:var(--leaf)}
.nav{position:absolute;top:44px;display:flex;font-size:15px;font-weight:600;color:var(--white)}
.nav span{position:absolute;white-space:nowrap}
.nav .active{color:var(--orange)}
.hero-line{left:112px;top:214px;width:170px;height:2px;background:var(--white)}
.welcome{left:300px;top:196px;font-family:"Playfair Display",serif;font-style:italic;font-size:28px;color:var(--white)}
.hero-title{left:110px;top:245px;font-size:56px;font-weight:700;color:var(--orange);white-space:nowrap}
.hero-text{left:114px;top:328px;width:490px;font-family:Arial,sans-serif;font-size:17px;line-height:30px;color:var(--white)}
.btn{position:absolute;display:flex;align-items:center;height:40px;border:2px solid var(--leaf);font-size:17px;font-weight:500;color:var(--orange);padding-left:10px}
.btn i{position:absolute;right:-2px;top:-2px;width:40px;height:40px;border-left:2px solid var(--leaf)}

/* Categories */
.cat{position:absolute;top:709px;width:228px;height:198px;background:var(--card);text-align:center}
.cat .disc{position:absolute;left:59px;top:20px;width:110px;height:110px;border-radius:50%;background:var(--white)}
.cat .disc svg{position:absolute;left:25px;top:25px}
.cat p{position:absolute;left:0;right:0;top:137px;font-size:17px;font-weight:500;color:var(--green)}
.arrow{position:absolute;width:31px;height:31px;border:1.5px solid #8a8a8a;border-radius:50%}
.arrow svg{position:absolute;left:8px;top:7px}

/* About */
.about{position:absolute;left:0;top:1030px;width:1200px;height:580px;background:var(--paper)}
.about-img{left:115px;top:1090px;width:375px;height:485px;background:radial-gradient(ellipse at 50% 55%,#d7dccf 0%,#eceee8 55%,var(--paper) 100%)}
.h2{font-size:40px;font-weight:700;color:var(--orange)}
.about-lead{left:599px;top:1180px;width:488px;font-size:19px;line-height:33px;text-align:justify;color:var(--ink)}
.about-body{left:601px;top:1294px;width:486px;font-size:15px;line-height:30px;text-align:justify;color:var(--muted)}

/* Products */
.band{position:absolute;left:0;top:1610px;width:1200px;height:330px;background:var(--green)}
.shop{position:absolute;left:111px;top:1808px;width:978px;height:518px;background:var(--white)}
.prod{position:absolute;top:1875px;width:261px}
.prod .img{height:251px}
.prod .row{position:absolute;left:2px;right:0;display:flex;justify-content:space-between;align-items:center}
.prod .name{top:264px;font-size:18px}
.stars{font-size:12px;letter-spacing:1px;color:#f2c200}
.prod .rule{position:absolute;left:0;right:0;top:300px;height:1px;background:#cfcfcf}
.prod .price{top:310px;font-size:17px}
.old{color:#aaa;text-decoration:line-through;margin-right:34px}

/* Blog */
.blog{position:absolute;left:0;top:2326px;width:1200px;height:650px;background:linear-gradient(180deg,#ffffff 0%,#f2f2f0 45%,#b5b8ae 80%,#55584e 100%)}
.post-img{position:absolute;top:2519px;width:456px;height:231px}
.post{position:absolute;top:2676px;width:367px;height:150px;background:var(--white);padding:20px 27px}
.post .meta{font-size:15px;color:#999}
.post .meta em{font-style:italic}
.post h3{margin-top:17px;font-size:18px;font-weight:500;letter-spacing:.5px}
.post a{display:inline-block;margin-top:22px;font-size:15px;color:#333;text-decoration:underline}

/* Footer */
.footer{position:absolute;left:0;top:2976px;width:1200px;height:320px;background:var(--footer)}
.fnav{position:absolute;top:3080px;font-size:15px;font-weight:600;color:var(--white)}
.social{position:absolute;top:3138px;width:16px;height:16px;border-radius:50%;background:var(--orange)}
.frule{left:111px;top:3236px;width:974px;height:1px;background:#555}
.copy{left:115px;top:3252px;font-size:16px;color:var(--white)}
</style>
</head>
<body>

<section class="hero">
  <div class="hero-photo" role="img" aria-label="Close-up photograph of green hemp leaves against a dark background"></div>
  <div class="topbar"></div>
  <div class="brand" style="left:111px;top:38px;font-size:26px"><span class="mark"></span>Meadowbright</div>
  <nav class="nav">
    <span class="active" style="left:349px">HOME <svg width="12" height="8" viewBox="0 0 12 8" style="margin-left:8px"><path d="M0 0h12L6 7z" fill="#f7a21b"/></svg></span>
    <span style="left:448px">ABOUT US</span>
    <span style="left:581px">BLOG</span>
    <span style="left:675px">PRODUCTS</span>
    <span style="left:814px">CONTACT US</span>
  </nav>
  <div class="abs" style="left:956px;top:30px;width:1px;height:40px;background:#666"></div>
  <svg class="abs" style="left:980px;top:38px" width="34" height="30" viewBox="0 0 34 30"><path d="M0 2h6l5 17h18l4-13H9" fill="none" stroke="#f7a21b" stroke-width="3"/><path d="M10 6h23l-4 13H11z" fill="#f7a21b"/><circle cx="13" cy="26" r="3" fill="#f7a21b"/><circle cx="27" cy="26" r="3" fill="#f7a21b"/></svg>
  <div class="abs" style="left:1042px;top:30px;width:1px;height:40px;background:#666"></div>
  <svg class="abs" style="left:1059px;top:38px" width="30" height="30" viewBox="0 0 30 30"><circle cx="12" cy="12" r="9" fill="none" stroke="#f7a21b" stroke-width="4"/><path d="M19 19l9 9" stroke="#f7a21b" stroke-width="5" stroke-linecap="round"/></svg>

  <div class="abs hero-line"></div>
  <div class="abs welcome">Welcome to</div>
  <h1 class="abs hero-title">Meadowbright Hemp</h1>
  <p class="abs hero-text">we have Cannabis products that are hemp derived and 100% legal across the US</p>
  <a class="btn" style="left:112px;top:418px;width:163px">Read more<i></i></a>
</section>

<div class="arrow" style="left:42px;top:800px"><svg width="14" height="16" viewBox="0 0 14 16"><path d="M10 1L3 8l7 7" fill="none" stroke="#777" stroke-width="1.5"/></svg></div>
<div class="arrow" style="left:1127px;top:800px"><svg width="14" height="16" viewBox="0 0 14 16"><path d="M4 1l7 7-7 7" fill="none" stroke="#777" stroke-width="1.5"/></svg></div>

<div class="cat" style="left:111px"><div class="disc"><svg width="60" height="60" viewBox="0 0 60 60" fill="none" stroke="#f7a21b" stroke-width="2.5"><path d="M30 56V18"/><path d="M30 34C18 34 12 24 12 16c10 0 18 8 18 18zM30 28c0-10 8-18 18-18 0 8-6 18-18 18z"/></svg></div><p>FRESH CANNABIS</p></div>
<div class="cat" style="left:360px"><div class="disc"><svg width="60" height="60" viewBox="0 0 60 60" fill="none" stroke="#f7a21b" stroke-width="2.5"><path d="M8 22h38v18a12 12 0 0 1-12 12H20A12 12 0 0 1 8 40z"/><path d="M46 28h4a6 6 0 0 1 0 12h-4M4 56h46"/></svg></div><p>CANNABIS FOOD</p></div>
<div class="cat" style="left:609px"><div class="disc"><svg width="60" height="60" viewBox="0 0 60 60" fill="none" stroke="#f7a21b" stroke-width="2.5"><circle cx="38" cy="20" r="14"/><path d="M28 30l20-20"/><rect x="4" y="34" width="30" height="14" rx="7" transform="rotate(-40 19 41)"/></svg></div><p>MEDICAL PILLS</p></div>
<div class="cat" style="left:858px"><div class="disc"><svg width="60" height="60" viewBox="0 0 60 60" fill="none" stroke="#f7a21b" stroke-width="2.5"><rect x="8" y="24" width="18" height="30" rx="3"/><path d="M12 24v-8h10v8M15 16V6h4v10"/><circle cx="42" cy="38" r="14"/></svg></div><p>MEDICAL PILLS</p></div>

<section class="about"></section>
<div class="abs about-img" role="img" aria-label="Amber dropper bottle of hemp oil on a hemp leaf beside a dish of ground seed"></div>
<h2 class="abs h2" style="left:600px;top:1100px">About Us</h2>
<p class="abs about-lead">Also that all cannabis is locally grown and products are extracted and made in house and sent out for third party lab testing</p>
<p class="abs about-body">Lorem ipsum dolor sit amet, consectetur adipiscing elit, sed do eiusmod tempor incididunt ut labore et dolore magna aliqua. Ut enim ad minim veniam, quis nostrud exercitation ullamco laboris nisi ut aliquip ex ea commodo consequat.</p>
<a class="btn" style="left:601px;top:1459px;width:164px">Read more<i></i></a>

<section class="band"></section>
<h2 class="abs h2" style="left:0;width:1200px;top:1697px;text-align:center">Our Amazing Cannabis Products</h2>
<div class="shop"></div>
<div class="arrow" style="left:42px;top:2024px"><svg width="14" height="16" viewBox="0 0 14 16"><path d="M10 1L3 8l7 7" fill="none" stroke="#777" stroke-width="1.5"/></svg></div>
<div class="arrow" style="left:1127px;top:2024px"><svg width="14" height="16" viewBox="0 0 14 16"><path d="M4 1l7 7-7 7" fill="none" stroke="#777" stroke-width="1.5"/></svg></div>

<div class="prod" style="left:178px">
  <div class="img" role="img" aria-label="Dark dropper bottles of tincture among hemp leaves" style="background:linear-gradient(160deg,#3a3a38,#1f2a1c 60%,#4a3018)"></div>
  <div class="row name">Lorem ipsum<span class="stars">★★★★★</span></div>
  <div class="rule"></div>
  <div class="row price"><span><span class="old">$24.95</span>$15.00</span><svg width="20" height="18" viewBox="0 0 34 30"><path d="M0 2h6l5 17h18l4-13H9" fill="none" stroke="#f7a21b" stroke-width="3"/><path d="M10 6h23l-4 13H11z" fill="#f7a21b"/><circle cx="13" cy="26" r="3" fill="#f7a21b"/><circle cx="27" cy="26" r="3" fill="#f7a21b"/></svg></div>
</div>
<div class="prod" style="left:475px">
  <div class="img" role="img" aria-label="Jar of hemp cream with dried flower buds" style="background:linear-gradient(160deg,#d8d6cf,#f1efea 50%,#9a9b84)"></div>
  <div class="row name">Lorem ipsum<span class="stars">★★★★★</span></div>
  <div class="rule"></div>
  <div class="row price"><span><span class="old">$24.95</span>$15.00</span><svg width="20" height="18" viewBox="0 0 34 30"><path d="M0 2h6l5 17h18l4-13H9" fill="none" stroke="#f7a21b" stroke-width="3"/><path d="M10 6h23l-4 13H11z" fill="#f7a21b"/><circle cx="13" cy="26" r="3" fill="#f7a21b"/><circle cx="27" cy="26" r="3" fill="#f7a21b"/></svg></div>
</div>
<div class="prod" style="left:765px">
  <div class="img" role="img" aria-label="Glass bottles of golden hemp oil beside hemp leaves" style="background:linear-gradient(160deg,#8fa012,#a9b418 50%,#c89a18)"></div>
  <div class="row name">Lorem ipsum<span class="stars">★★★★★</span></div>
  <div class="rule"></div>
  <div class="row price"><span><span class="old">$24.95</span>$15.00</span><svg width="20" height="18" viewBox="0 0 34 30"><path d="M0 2h6l5 17h18l4-13H9" fill="none" stroke="#f7a21b" stroke-width="3"/><path d="M10 6h23l-4 13H11z" fill="#f7a21b"/><circle cx="13" cy="26" r="3" fill="#f7a21b"/><circle cx="27" cy="26" r="3" fill="#f7a21b"/></svg></div>
</div>

<section class="blog" role="img" aria-label="Soft background of hemp plants growing in soil"></section>
<h2 class="abs h2" style="left:0;width:1200px;top:2420px;text-align:center">Blog</h2>
<div class="arrow" style="left:42px;top:2644px"><svg width="14" height="16" viewBox="0 0 14 16"><path d="M10 1L3 8l7 7" fill="none" stroke="#777" stroke-width="1.5"/></svg></div>
<div class="arrow" style="left:1127px;top:2644px"><svg width="14" height="16" viewBox="0 0 14 16"><path d="M4 1l7 7-7 7" fill="none" stroke="#777" stroke-width="1.5"/></svg></div>
<div class="post-img" style="left:138px;background:linear-gradient(180deg,#f0eeea,#c9b9a0 60%,#6b6a3a)" role="img" aria-label="Small bottles of oil and jars of dried hemp flower"></div>
<div class="post-img" style="left:609px;background:linear-gradient(180deg,#efece7,#c8b192 60%,#7a5a30)" role="img" aria-label="Dropper bottles and a jar of dried hemp flower on a table"></div>
<article class="post" style="left:185px"><p class="meta">Lorem ipsum dolor &nbsp;/ <em>January 4, 2023</em></p><h3>LOREM IPSUM DOLOR</h3><a>READ MORE</a></article>
<article class="post" style="left:656px"><p class="meta">Lorem ipsum dolor &nbsp;/ <em>January 5, 2023</em></p><h3>LOREM IPSUM DOLOR</h3><a>READ MORE</a></article>

<footer class="footer"></footer>
<div class="brand" style="left:111px;top:3098px;font-size:36px"><span class="mark" style="width:30px;height:30px"></span>Meadowbright</div>
<span class="fnav" style="left:523px">HOME</span>
<span class="fnav" style="left:622px">ABOUT US</span>
<span class="fnav" style="left:755px">BLOG</span>
<span class="fnav" style="left:848px">PRODUCTS</span>
<span class="fnav" style="left:988px">CONTACT US</span>
<span class="social" style="left:862px"></span>
<span class="social" style="left:904px"></span>
<span class="social" style="left:946px"></span>
<span class="social" style="left:988px"></span>
<span class="social" style="left:1030px"></span>
<span class="social" style="left:1072px"></span>
<div class="abs frule"></div>
<p class="abs copy">© 2023 &nbsp;Meadowbright Hemp</p>

</body>
</html>
```